KAY VELORE

We need a letterhead design for an Image & Etiquette Consultancy company based in Singapore.

The services we provide are Personal Image Consultation, Image & Etiquette Workshop for schools and corporate.

The design should have our corporate colour as seen in the logo files I have uploaded.

Since our company helps clients with their image, the design should be aesthetically very appealing. It should reflect a very classy & elegant feel.

I will print the letterhead using my printer but most of the time will use it to write letters to my clients therefore the format should include MS Word.

```html
<!DOCTYPE html>
<html lang="en">
<head>
<meta charset="utf-8">
<title>Kay Velore Letterhead</title>
<link href="https://fonts.googleapis.com/css2?family=Open+Sans:wght@400&display=swap" rel="stylesheet">
<style>
  :root {
    --backdrop: #dccdb3;
    --paper: #ffffff;
    --plum: #330d48;
    --gold: #d9a630;
    --ink: #1e1e1e;
    --footer-ink: #3b1a52;
  }
  * { margin: 0; padding: 0; box-sizing: border-box; }
  html, body {
    width: 1200px; height: 1000px; overflow: hidden;
    background: var(--backdrop);
  }
  .letterhead {
    position: absolute; left: 262px; top: 20px;
    width: 676px; height: 960px;
    background: var(--paper);
    box-shadow: 0 6px 24px rgba(80, 60, 30, 0.18);
    font-family: "Open Sans", Arial, sans-serif;
    color: var(--ink);
  }
  .header-band {
    height: 150px; background: var(--plum);
    padding: 56px 0 0 70px;
  }
  .brand-name {
    font-family: "Open Sans", Arial, sans-serif;
    font-weight: 400; font-size: 32px; letter-spacing: 1px;
    color: var(--gold); line-height: 1;
  }
  .letter-body {
    padding: 52px 70px 0 90px;
    font-size: 11px; line-height: 1.55;
  }
  .letter-date { margin-bottom: 14px; }
  .recipient { margin-bottom: 14px; }
  .letter-text { text-align: justify; margin-bottom: 22px; }
  .closing { margin-bottom: 20px; }
  .footer-rule {
    position: absolute; left: 60px; right: 60px; top: 860px;
    height: 1px; background: var(--footer-ink);
  }
  .contact-list {
    position: absolute; top: 878px; left: 220px;
    display: grid; grid-template-columns: 200px 220px; row-gap: 6px;
    font-size: 9.5px; color: var(--footer-ink); font-style: normal;
  }
  .contact-item { display: flex; align-items: center; gap: 7px; }
  .contact-item svg { width: 11px; height: 11px; fill: var(--footer-ink); flex: none; }
</style>
</head>
<body>
<main class="letterhead">
  <header class="header-band">
    <div class="brand-name">KAY VELORE</div>
  </header>

  <section class="letter-body">
    <p class="letter-date">April 28. 2014</p>
    <p class="recipient">Alan Reeve,<br>58 Orchard Lane,<br>Somewhere.</p>
    <p>Dear Ms Reeve,</p>
    <p class="letter-text">Lorem ipsum dolor sit amet, consectetur adipiscing elit. Vestibulum sollicitudin rhoncus molestie. Etiam sed libero ultricies, cursus nisl at, scelerisque diam. Aliquam erat volutpat. Phasellus vel dignissim eros. Nullam eu lorem fermentum, porta magna a, sodales massa. Lorem ipsum dolor sit amet, consectetur adipiscing elit. Duis mollis, tortor sit amet mattis suscipit, nulla quam dictum enim, at maximus sapien ante vitae massa. Maecenas molestie neque vel purus fringilla, id consectetur sapien volutpat. Sed imperdiet bibendum tellus, a feugiat diam finibus nec. Lorem ipsum dolor sit amet, consectetur adipiscing elit. Pellentesque blandit quam vitae nibh mattis, in euismod mi tempor. Aenean pulvinar scelerisque turpis, fermentum pharetra arcu commodo quis. Donec vitae orci pulvinar, faucibus felis id, gravida dolor. Morbi at faucibus ante, dictum varius elit. Nulla purus eros, cursus sit amet scelerisque a, condimentum aliquam est. Nulla sed nulla sagittis, tempor massa non, volutpat libero. Quisque sed semper elit, vitae mattis dolor. Fusce tellus orci, mattis eu orci sed, facilisis sollicitudin velit. In porttitor lectus velit, eget auctor augue euismod quis. Suspendisse in libero ut nunc ultricies posuere non ac ipsum. Fusce consequat elementum turpis, eu feugiat purus molestie lacinia.</p>
    <p class="closing">Sincerely</p>
    <p>Mr. Reeve</p>
  </section>

  <div class="footer-rule"></div>

  <address class="contact-list">
    <div class="contact-item">
      <svg viewBox="0 0 12 12" aria-hidden="true"><path d="M6 0a4 4 0 0 0-4 4c0 3 4 8 4 8s4-5 4-8a4 4 0 0 0-4-4zm0 5.6A1.6 1.6 0 1 1 6 2.4a1.6 1.6 0 0 1 0 3.2z"/></svg>
      Address: To be confirmed
    </div>
    <div class="contact-item">
      <svg viewBox="0 0 12 12" aria-hidden="true"><path d="M1 3h10v7H1zM3 1h6v2H3z"/></svg>
      Fax: To be confirmed
    </div>
    <div class="contact-item">
      <svg viewBox="0 0 12 12" aria-hidden="true"><path d="M3.5 0h5a1 1 0 0 1 1 1v10a1 1 0 0 1-1 1h-5a1 1 0 0 1-1-1V1a1 1 0 0 1 1-1zm.5 1.5v8h4v-8z"/></svg>
      Phone: To be confirmed
    </div>
    <div class="contact-item">
      <svg viewBox="0 0 12 12" aria-hidden="true"><path d="M0 2h12v8H0zm1 1v.4l5 3.3 5-3.3V3z"/></svg>
      Email: hello@kayvelore.example
    </div>
  </address>
</main>
</body>
</html>
```